Commercial Rooftop Solar business needs a website

We need a website with fantastic appeal for a new company based in Melbourne called Tidewell Energy. We design and install solar energy systems for commercial applications across Australia. Our market is to focus on small to medium businesses looking for solar solutions, but we will also provide our service for residential customers. We would like a beautiful 'front page' feel to our home page, using photographs of solar PV systems and/or natural imagery. Our logo uses the colours orange and black, which could easily be echoed in photographic imagery of sunset and sunrise, for example. The design should communicate quiet confidence and professionalism to a corporate marketplace.

NEW POINTS FOR BRIEF: This design also needs to be flexible to allow for additional future content, including a Support page with sub pages, FAQ's, and a Blog.

As part of this design project, we will require the coding for the website to be completed by the designer.

We have seen some websites, which we like the look and feel of: these are listed below.

brightquarrypower.com.au:

• Beautiful images underlaying brief text selling points.
• Simple ‘front cover’ style home page with elegant drop-down menu, stylish simple font style.
• Home page invites exploration through the menu links, rather than trying to provide all the information up front.
• Company logo and name in the top left hand corner, contact details accessible at top right hand, seems consistent in most sites.

fonvaleenergy.com.au

murlockenergy.com:
• Same element as the others is the front-page style home page with beautiful images underlying text.

We have a webpage that we started uploading content to. You can use some of the content there in your designs: www.tidewellenergy.com.au

Technical Specifications:
PAGES:

Home

About Us

Solutions - Commercial
- Residential

Products - Solar Panels - Vorla Kestrel, Vorla TUSK, Vorla QB
- Solar Inverters - Delmark, VoltHaven
- Monitoring systems - Grid Insight
- Batteries - KD

- Datasheets have been provided for reference but if it's too much work, you can use generic text and we will provide content later.

Contact Us

FUTURE PAGES (Please consider in structure, where links could be placed):

Support

FAQ's

Blog.

We could provide some content for the Support page soon, but the Blog and FAQ's are future pages which we don't want highlighted in the design as we don't yet have content.

Phone: 1800 7 TIDEW
Email: sales@tidewellenergy.com.au

Currently, I do not have images and text available. Please
use placeholders in the meantime. The final text and images will be uploaded for the winner once a winning design has been selected.

Target Market(s)

Primary focus is on small to medium sized business owners. Those owners will have a house which may be suitable for solar so we want to cater to residential deeper in the website.

Industry/Entity Type

Solar Energy

Coding

Coded - Design and coding required

Number of Pages Required

5+ page

Colors
f78f20
0255a3

Requirements
Must have
• Logo as per attachments.
Nice to have
• Logo can have alternate colours Eg. White on Orange or Black etc. provided colour correct logo is shown somewhere eg. footer or contact page.
• In the active site, I'd like to have:
• Very slowly zooming images - barely perceptible.
• Title text that rolls into place
• Subtle movements
• See https://pellbrook.com.au/ for example

```html
<!DOCTYPE html>
<html lang="en">
<head>
<meta charset="utf-8">
<title>Tidewell Energy — Commercial Solar</title>
<link href="https://fonts.googleapis.com/css2?family=Maven+Pro:wght@400;500;700&family=Open+Sans:ital,wght@0,400;0,600;0,700;1,400&display=swap" rel="stylesheet">
<style>
:root{
  --orange:#f78f20;
  --blue:#0255a3;
  --ink:#222;
  --text:#555;
  --muted:#888;
  --line:#e3e3e3;
  --footer:#1c1c1c;
  --white:#fff;
}
*{box-sizing:border-box;margin:0;padding:0}
html,body{width:1200px;height:3830px;overflow:hidden}
body{position:relative;background:var(--white);font-family:"Open Sans",sans-serif;color:var(--text)}
.abs{position:absolute}
h2.section-title{position:absolute;left:0;width:1200px;text-align:center;font-family:"Maven Pro",sans-serif;font-weight:700;color:var(--orange);font-size:21px;letter-spacing:.5px}
.btn{display:inline-block;background:var(--orange);color:#fff;border-radius:20px;font-family:"Maven Pro",sans-serif;font-size:11px;font-weight:500;text-align:center}

.site-header{position:absolute;top:0;left:0;width:1200px;height:77px;background:#fff;z-index:5}
.brand{position:absolute;left:26px;top:22px;display:flex;align-items:center;gap:8px;font-family:"Maven Pro",sans-serif;font-weight:700;font-size:16px;color:var(--ink);letter-spacing:1px}
.brand i{width:14px;height:14px;border-radius:50%;background:var(--orange);display:block}
.main-nav{position:absolute;right:155px;top:34px;display:flex;gap:25px;font-family:"Maven Pro",sans-serif;font-size:12px;color:var(--ink)}
.main-nav .active{color:var(--orange);position:relative}
.main-nav .active:after{content:"";position:absolute;left:0;right:0;bottom:-6px;height:2px;background:var(--orange)}
.contact-btn{position:absolute;right:20px;top:28px;width:104px;height:30px;line-height:30px;font-size:12px}
.dropdown{position:absolute;left:817px;top:71px;width:150px;background:var(--orange);padding:8px 10px;z-index:6;list-style:none;font-size:10px;color:#fff;line-height:19px}
.dropdown .hover{font-weight:700}

.hero{position:absolute;top:77px;left:0;width:1200px;height:548px;background:linear-gradient(180deg,#4e5a66 0%,#5b6670 40%,#3d4650 75%,#2a3038 100%)}
.hero-shade{position:absolute;inset:0;background:rgba(0,0,0,.25)}
.hero-copy{position:absolute;top:248px;width:1200px;text-align:center;color:#fff;font-family:"Maven Pro",sans-serif}
.hero-copy .lead{font-family:"Open Sans",sans-serif;font-style:italic;font-size:16px}
.hero-copy .big{font-size:30px;line-height:36px;margin-top:4px}
.hero-copy .big b{font-weight:700}
.hero .btn{position:absolute;left:552px;top:479px;width:96px;height:24px;line-height:24px;font-size:10px}
.hero .chev{position:absolute;left:588px;top:520px}
.hero-dots{position:absolute;left:1165px;top:452px;display:flex;flex-direction:column;gap:8px}
.hero-dots i{width:8px;height:8px;border-radius:50%;border:1.5px solid #fff;display:block}
.hero-dots i.on{background:var(--orange);border-color:var(--orange)}

.about-kicker{position:absolute;top:668px;width:1200px;text-align:center;font-size:10px;color:var(--text);letter-spacing:1px}
.about-cols{position:absolute;top:738px;left:89px;width:1022px;display:flex;gap:26px;font-size:10.5px;line-height:15px}
.about-cols div{flex:1}
.about-cols p{margin-bottom:11px}
.about-cols b{color:var(--ink)}
.about-cols a{color:var(--orange)}
.read-more{position:absolute;left:552px;top:928px;width:96px;height:26px;line-height:26px;font-size:10px}

.commercial{position:absolute;top:985px;left:0;width:1200px;height:400px}
.commercial h2{position:absolute;top:88px;width:1200px;text-align:center;color:#fff;font-family:"Maven Pro",sans-serif;font-weight:700;font-size:20px}
.feature{position:absolute;top:152px;width:220px;text-align:center;color:#fff;font-family:"Maven Pro",sans-serif;font-weight:700;font-size:10.5px;line-height:14px}
.feature .ico{width:74px;height:74px;border-radius:50%;background:var(--orange);margin:0 auto 22px;display:flex;align-items:center;justify-content:center}

.product{position:absolute;top:1455px;width:236px;text-align:center}
.panel{margin:0 auto;height:166px;border-radius:2px}
.product h3{font-family:"Maven Pro",sans-serif;font-size:18px;line-height:22px;color:var(--ink);margin-top:36px;font-weight:400}
.product h3 b{font-weight:700}
.product p{text-align:left;font-size:10px;line-height:14px;margin-top:14px;height:124px}
.dl{display:flex;align-items:center;gap:8px;width:180px;height:32px;border-radius:16px;background:var(--orange);color:#fff;padding-left:14px;font-size:8.5px;line-height:11px;text-align:left}
.video-title{position:absolute;top:1968px;font-family:"Maven Pro",sans-serif;font-weight:700;font-size:17px;color:var(--ink);text-align:center}
.video{position:absolute;top:2017px;height:194px}
.video .bar{position:absolute;left:10px;right:10px;bottom:10px;height:3px;background:rgba(255,255,255,.5)}
.video .bar i{display:block;width:30%;height:100%;background:var(--orange)}

.blog{position:absolute;top:2250px;left:0;width:1200px;height:400px}
.blog-card-img{position:absolute;top:2395px;width:148px;height:148px}
.blog-card{position:absolute;top:2392px;width:280px}
.blog-card h4{font-family:"Maven Pro",sans-serif;font-weight:700;font-size:15px;line-height:19px;color:var(--ink)}
.blog-card .meta{font-size:8px;color:var(--muted);margin:6px 0 8px}
.blog-card p{font-size:10px;line-height:13.5px;color:var(--ink)}
.blog-dots{position:absolute;top:2583px;left:577px;display:flex;gap:6px}
.blog-dots i{width:8px;height:8px;border-radius:50%;border:1.5px solid var(--muted);display:block}
.blog-dots i.on{background:var(--orange);border-color:var(--orange)}

.faq{position:absolute;top:2750px;left:243px;width:717px;list-style:none;font-family:"Maven Pro",sans-serif;color:var(--text);font-size:13px}
.faq li{border-bottom:1px solid var(--line);padding:18px 6px;display:flex;justify-content:space-between;align-items:flex-start;flex-wrap:wrap}
.faq .pm{color:var(--orange);font-size:18px;line-height:14px}
.faq li.open .q{font-weight:700;color:var(--ink)}
.faq .a{width:100%;font-family:"Open Sans",sans-serif;font-size:10px;line-height:14px;margin-top:16px}
.faq .a p{margin-bottom:10px}

.clients-title{position:absolute;top:3264px;width:1200px;text-align:center;font-family:"Maven Pro",sans-serif;font-weight:700;font-size:19px;color:var(--ink)}
.clients{position:absolute;top:3350px;left:185px;width:830px;display:flex;justify-content:space-between;align-items:center}
.client{display:flex;align-items:center;gap:6px;font-family:"Maven Pro",sans-serif;font-weight:700;font-size:12px;color:#333;line-height:13px}
.client i{width:22px;height:22px;border-radius:50%;background:var(--orange);display:block}
.client i.b{background:var(--blue)}

.footer{position:absolute;top:3460px;left:0;width:1200px;height:331px}
.footer-bg{position:absolute;inset:0;background:linear-gradient(180deg,#222 0%,#161616 100%)}
.footer-brand{position:absolute;left:250px;top:78px;font-family:"Maven Pro",sans-serif;font-weight:700;font-size:15px;color:#fff;letter-spacing:1px}
.footer-about{position:absolute;left:428px;top:40px;width:158px;font-size:8px;line-height:11px;color:#ccc}
.fcol{position:absolute;top:138px;font-size:8.5px;line-height:12px;color:#ccc}
.fcol h5{font-family:"Maven Pro",sans-serif;font-size:9.5px;color:#fff;margin-bottom:10px;letter-spacing:.5px}
.fcol ul{list-style:none}
.fcol b{color:var(--orange);font-weight:600}
.socials{display:flex;gap:7px}
.socials i{width:10px;height:10px;border-radius:50%;background:#fff;display:block}
.form-title{position:absolute;left:613px;top:36px;font-family:"Maven Pro",sans-serif;font-size:10px;color:#fff;letter-spacing:.5px}
.field{position:absolute;height:24px;background:#2e2e2e;border:1px solid #3a3a3a;font-size:8px;color:#999;padding:6px 8px}
.send{position:absolute;left:613px;top:258px;width:90px;height:22px;line-height:22px;font-size:9px;border-radius:3px}
.bottom-bar{position:absolute;top:3791px;left:0;width:1200px;height:39px;background:#0f0f0f;color:#aaa;font-size:8px;line-height:39px;padding-left:250px}
</style>
</head>
<body>

<header class="site-header">
  <div class="brand"><i></i>TIDEWELL ENERGY</div>
  <nav class="main-nav">
    <span>Home</span><span>About Us</span><span>Solutions</span><span class="active">Products</span><span>Blog</span><span>FAQ's</span><span>Support</span>
  </nav>
  <span class="btn contact-btn">Contact Us</span>
</header>
<ul class="dropdown">
  <li>Solar Panels</li>
  <li>Vorla Kestrel, Vorla QB, Vorla TUSK</li>
  <li class="hover">Solar Inverters</li>
  <li>Delmark, VoltHaven</li>
  <li>Monitoring Systems</li>
  <li>Grid Insight</li>
  <li>Batteries</li>
  <li>KD</li>
</ul>

<section class="hero" role="img" aria-label="Aerial photo of a waterfront home with rooftop solar panels">
  <div class="hero-shade"></div>
  <div class="hero-copy">
    <p class="lead">Tidewell Energy are currently developing a slick new website.</p>
    <p class="big">Come back soon or<br><b>USE THE CONTACT FORM FOR ENQUIRIES.</b></p>
  </div>
  <span class="btn">Learn More</span>
  <svg class="chev" width="24" height="14" viewBox="0 0 24 14"><path d="M2 2l10 9 10-9" fill="none" stroke="#fff" stroke-width="3"/></svg>
  <div class="hero-dots"><i></i><i></i><i></i><i class="on"></i></div>
</section>

<p class="about-kicker">ABOUT US</p>
<h2 class="section-title" style="top:690px">TIDEWELL ENERGY</h2>
<div class="about-cols">
  <div>
    <p><b>Tidewell Energy</b> is a national company that specialises in solar solutions for the commercial market. We also provide solutions for the residential market, bringing our uncompromising quality and service to the home.</p>
    <p>The founder of the company has over 10 years experience delivering projects on both a residential and commercial scale, having overseen the installation of more than 3 megawatts of solar projects. They were a pioneer on the <a>first megawatt rooftop project</a> in Australia.</p>
    <p>As a leader in the field, we offer cutting edge solar technology backed by industry leading warranties. All our systems are designed and installed by <a>Brightgrid Council</a> accredited persons. Our award winning designer will ensure your system will give the best long term performance and return on investment.</p>
  </div>
  <div>
    <p>Our commercial team specialises in projects from 10 kilowatts to 3 megawatts. We have partnered with Murlock Energy who have more than 10 years experience delivering commercial projects. <a>Murlock Energy</a> provides engineering, technical support and project management of the highest standard within the commercial solar sector. Together we have experience in the unique requirements of business needs and commercial building codes.</p>
    <p>One size does NOT fit all and we welcome the opportunity to assist in providing a tailored solution for your home or business.</p>
  </div>
</div>
<span class="btn read-more">Read More</span>

<section class="commercial">
  <svg class="abs" style="left:0;top:0" width="1200" height="400" role="img" aria-label="Close-up photo of blue solar panels under sky">
    <defs><linearGradient id="panelSky" x1="0" y1="0" x2="1" y2="1"><stop offset="0" stop-color="#2f74c4"/><stop offset=".5" stop-color="#1d5aa6"/><stop offset="1" stop-color="#113d78"/></linearGradient></defs>
    <polygon points="0,65 1200,5 1200,395 0,345" fill="url(#panelSky)"/>
  </svg>
  <h2>COMMERCIAL SOLAR</h2>
  <div class="feature" style="left:195px">
    <div class="ico"><svg width="36" height="36" viewBox="0 0 36 36" fill="none" stroke="#fff" stroke-width="2.5"><circle cx="18" cy="12" r="5"/><path d="M18 2v3M8 12H5M31 12h-3M10 5l2 2M26 5l-2 2"/><path d="M6 32l4-12h16l4 12z"/></svg></div>
    TIDEWELL ENERGY SPECIALISES<br>IN ENERGY SOLUTIONS FOR SMALL<br>TO MEDIUM BUSINESSES
  </div>
  <div class="feature" style="left:490px">
    <div class="ico"><svg width="34" height="34" viewBox="0 0 34 34" fill="none" stroke="#fff" stroke-width="2.5"><rect x="6" y="4" width="22" height="26"/><path d="M11 11h12M11 17h12M11 23h8"/></svg></div>
    BUSINESS CASE<br>NO-COST SOLAR.
  </div>
  <div class="feature" style="left:785px">
    <div class="ico"><svg width="34" height="34" viewBox="0 0 34 34" fill="none" stroke="#fff" stroke-width="2.5"><path d="M17 22c-8-2-9-10-8-15 6 0 12 3 8 15zM17 22c2-6 7-9 11-8-1 5-5 9-11 8z"/><path d="M4 28h9l6 2h11"/></svg></div>
    SUSTAINABILITY: OUR<br>ENVIRONMENT MATTERS.
  </div>
</section>

<h2 class="section-title" style="top:1402px">PRODUCTS</h2>
<div class="product" style="left:243px">
  <div class="panel" style="width:108px;background:linear-gradient(180deg,#2b3e6b,#1b2a4d)" role="img" aria-label="Vorla Kestrel solar panel"></div>
  <h3><b>VORLA KESTREL</b> - THE<br>BUDGET WORKHORSE</h3>
  <p>The Vorla Kestrel Series is the first PID-free module in the world. It can be used for all applications, however, it is especially ideal for installations in Australian places aware of its performance in high temperature. World's first double 85 certified PID-free module ensures highest reliability under all extreme conditions.</p>
  <div class="dl"><svg width="14" height="16" viewBox="0 0 14 16"><path d="M2 1h7l3 3v11H2z" fill="none" stroke="#fff" stroke-width="1.5"/></svg><span>Datasheet - Vorla Kestrel.pdf<br><b>Download File</b></span></div>
</div>
<div class="product" style="left:507px">
  <div class="panel" style="width:92px;background:linear-gradient(180deg,#30426e,#1c2b4f)" role="img" aria-label="Vorla QB solar panel with module badge"></div>
  <h3><b>VORLA QB</b> -<br>OPTIMISED AND FLEXIBLE</h3>
  <p>Vorla Solar recently partnered with Corvane Circuits, a cutting edge chip manufacturer, to develop the Vorla QB panel. The QB chip isn't like a standard optimiser, as it's actually installed into the panel and replaces each of the bypass diodes.</p>
  <div class="dl"><svg width="14" height="16" viewBox="0 0 14 16"><path d="M2 1h7l3 3v11H2z" fill="none" stroke="#fff" stroke-width="1.5"/></svg><span>Datasheet - Vorla QB.pdf<br><b>Download File</b></span></div>
</div>
<div class="product" style="left:770px">
  <div class="panel" style="width:104px;background:linear-gradient(180deg,#262a30,#131518)" role="img" aria-label="Vorla TUSK black solar panel"></div>
  <h3><b>VORLA TUSK</b> -<br>BEAUTIFUL POWER</h3>
  <p>Vorla TUSK panels are high efficiency panels with a beautiful black frame. A layer on the back of the cells helps to reflect light that passes through the cell, back into the cell so it can generate more power.</p>
  <div class="dl"><svg width="14" height="16" viewBox="0 0 14 16"><path d="M2 1h7l3 3v11H2z" fill="none" stroke="#fff" stroke-width="1.5"/></svg><span>Datasheet - Vorla TUSK.pdf<br><b>Download File</b></span></div>
</div>

<div class="video-title" style="left:235px;width:357px">VORLA QB</div>
<div class="video-title" style="left:684px;width:281px">VORLA TUSK</div>
<div class="video" style="left:235px;width:357px;background:linear-gradient(180deg,#6a717b,#3a3f47)" role="img" aria-label="Video still of a trade show stand presenting the Vorla QB panel"><div class="bar"><i></i></div></div>
<div class="video" style="left:684px;width:281px;background:linear-gradient(180deg,#1e2230,#0c0e14)" role="img" aria-label="Video still of black panels on a stage presentation"><div class="bar"><i></i></div></div>

<section class="blog">
  <svg class="abs" style="left:0;top:0" width="1200" height="400" role="img" aria-label="Faded photo of rooftop solar array">
    <defs><linearGradient id="blogBg" x1="0" y1="0" x2="0" y2="1"><stop offset="0" stop-color="#d9d9d9"/><stop offset="1" stop-color="#f1f1f1"/></linearGradient></defs>
    <polygon points="0,60 1200,5 1200,330 0,395" fill="url(#blogBg)"/>
  </svg>
</section>
<h2 class="section-title" style="top:2326px">BLOG</h2>
<div class="blog-card-img" style="left:133px;background:linear-gradient(135deg,#6f8fb2,#33506f)" role="img" aria-label="Installer working on solar panels"></div>
<div class="blog-card" style="left:303px">
  <h4>Lorem Ipsum is simply dummy text of the printing and typesetting industry.</h4>
  <p class="meta">Posted by Sean / Blog / 0 Comment</p>
  <p>Lorem Ipsum is simply dummy text of the printing and typesetting industry. Lorem Ipsum has been the industry's standard dummy text ever since the 1500s, when an unknown printer took a galley of type and scrambled it to make a type specimen book.</p>
</div>
<div class="blog-card-img" style="left:613px;background:linear-gradient(180deg,#9cc4e4,#4a7fb0)" role="img" aria-label="Wind turbines beside solar panels under blue sky"></div>
<div class="blog-card" style="left:787px">
  <h4>Lorem Ipsum is simply dummy text of the printing and typesetting industry.</h4>
  <p class="meta">Posted by Sean / Blog / 0 Comment</p>
  <p>Lorem Ipsum is simply dummy text of the printing and typesetting industry. Lorem Ipsum has been the industry's standard dummy text ever since the 1500s, when an unknown printer took a galley of type and scrambled it to make a type specimen book.</p>
</div>
<div class="blog-dots"><i class="on"></i><i></i><i></i><i></i></div>

<h2 class="section-title" style="top:2674px">FAQ</h2>
<ul class="faq">
  <li><span class="q">Lorem Ipsum is simply dummy text of the printing and typesetting industry.</span><span class="pm">+</span></li>
  <li class="open"><span class="q">Lorem Ipsum is simply dummy text of industry.</span><span class="pm">−</span>
    <div class="a"><p>Lorem Ipsum has been the industry's standard dummy text ever since the 1500s, when an unknown printer took a galley of type and scrambled it to make a type specimen book. It has survived not only five centuries, but also the leap into electronic typesetting, remaining essentially unchanged.</p><p>Lorem Ipsum has been the industry's standard dummy text ever since.</p></div></li>
  <li><span class="q">Lorem Ipsum is simply dummy text of the printing.</span><span class="pm">+</span></li>
  <li><span class="q">Lorem Ipsum is simply dummy text of the printing industry.</span><span class="pm">+</span></li>
  <li><span class="q">Lorem Ipsum is simply dummy text of the printing and typesetting industry.</span><span class="pm">+</span></li>
  <li><span class="q">Lorem Ipsum is simply dummy text of industry.</span><span class="pm">+</span></li>
</ul>

<h2 class="clients-title">WHAT OUR CLIENTS SAY</h2>
<div class="clients">
  <div class="client"><i></i>BRIGHTGRID<br>COUNCIL</div>
  <div class="client"><i></i>SUNWARD GUILD</div>
  <div class="client"><i class="b"></i>SOUTHERN<br>PV FORUM</div>
  <div class="client"><i class="b"></i>Powerlean</div>
  <div class="client"><i class="b"></i>AMPWELL</div>
  <div class="client">Northfield Solar</div>
</div>

<footer class="footer">
  <div class="footer-bg" role="img" aria-label="Dark faded photo of solar panels"></div>
  <div class="footer-brand">TIDEWELL ENERGY</div>
  <p class="footer-about">Lorem Ipsum is simply dummy text of the printing and typesetting industry. Lorem Ipsum has been the industry's standard dummy text ever since the 1500s, when an unknown printer took a galley of type and scrambled it to make a type specimen book.</p>
  <div class="fcol" style="left:250px"><h5>LINK</h5><ul><li>› Home</li><li>› About Us</li><li>› Solutions</li><li>› Products</li><li>› Blog</li><li>› FAQ's</li><li>› Support</li><li>› Contact Us</li></ul></div>
  <div class="fcol" style="left:332px;width:160px"><h5>CONTACT</h5><p><b>Email:</b> sales@tidewellenergy.com.au</p><p style="margin-top:8px"><b>Phone:</b> 1800 7 TIDEW</p><p style="margin-top:8px"><b>Address:</b> 24 Harbour Lane, Melbourne</p></div>
  <div class="fcol" style="left:495px"><h5>SOCIAL MEDIA</h5><div class="socials"><i></i><i></i><i></i><i></i><i></i></div></div>
  <div class="form-title">CONTACT US</div>
  <div class="field" style="left:613px;top:64px;width:160px">Name</div>
  <div class="field" style="left:786px;top:64px;width:164px">Email</div>
  <div class="field" style="left:613px;top:98px;width:160px">Company Name</div>
  <div class="field" style="left:786px;top:98px;width:164px">Site Address</div>
  <div class="field" style="left:613px;top:132px;width:337px">Subject</div>
  <div class="field" style="left:613px;top:166px;width:337px;height:78px">Comment</div>
  <span class="btn send">Send Message</span>
</footer>
<div class="bottom-bar">© 2017 Tidewell Energy - ALL RIGHTS RESERVED</div>

</body>
</html>
```